IT Consulting Business Card Design

We need a business card on our company name....which is a IT consulting and staffing company. We also train masters graduates in various IT courses. 70% of the time these cards will be handed out to the graduate students at the universities. 30% for our clients and business partners. We are uploading our company logo...would like to see something that matches our logo or blends with it. Please visit www.brivolentaxis.com for more details on logo and colors.

Target Market(s)

70% of the time these cards will be handed out to the graduate students at the universities. 30% for our clients and business partners.

Industry/Entity Type

Business

Contact Information for Business Card

Tomas Verlinde
Vice-President
Brivolen Taxis Inc
3187 Corwick Lane, Suite 412
Ashbury Falls, NJ 07999
tomas@brivolentaxis.com
Office : 1-855-555-0148 X 312
Cell number : 908-555-0193

Requirements
Nice to have
• may be company logo and name on the back of the card and detials on the other side...just a thought..!!

```html
<!DOCTYPE html>
<html lang="en">
<head>
<meta charset="utf-8">
<title>Brivolen Taxis Inc — Business Card</title>
<link rel="stylesheet" href="https://fonts.googleapis.com/css2?family=Lato:wght@400;700;900&display=swap">
<style>
  :root {
    --backdrop: #3a3330;
    --card: #1b1b1b;
    --red: #e3212b;
    --white: #ffffff;
    --grey: #9a9a9a;
    --grey-light: #bdbdbd;
    --swoosh: #555555;
  }
  * { margin: 0; padding: 0; box-sizing: border-box; }
  html, body { width: 1200px; height: 832px; overflow: hidden; }
  body {
    background: var(--backdrop);
    font-family: "Lato", Arial, sans-serif;
    position: relative;
  }
  .card {
    position: absolute;
    width: 600px;
    height: 343px;
    background: var(--card);
    box-shadow: 0 10px 30px rgba(0,0,0,0.45);
    overflow: hidden;
  }
  .card--front { left: 130px; top: 80px; }
  .card--back { left: 470px; top: 410px; }

  /* front */
  .front-art { position: absolute; inset: 0; width: 100%; height: 100%; }
  .holder {
    position: absolute; right: 30px; top: 22px; text-align: right;
  }
  .holder__name {
    color: var(--white); font-size: 19px; font-weight: 700; letter-spacing: 0.3px;
  }
  .holder__title {
    color: var(--red); font-size: 11px; font-weight: 900; letter-spacing: 1px; margin-top: 2px;
  }
  .contact {
    position: absolute; right: 30px; top: 178px; text-align: right;
    color: var(--grey); font-size: 11.5px; line-height: 15px; letter-spacing: 0.4px;
  }
  .contact__label { font-weight: 700; color: var(--grey-light); }
  .brand {
    font-weight: 900; letter-spacing: 0.5px; color: var(--red); white-space: nowrap;
  }
  .brand--front { position: absolute; right: 30px; top: 240px; font-size: 24px; }

  /* back */
  .back-mark {
    position: absolute; left: 50%; top: 34px; transform: translateX(-50%);
    width: 130px; height: 130px;
  }
  .brand--back {
    position: absolute; left: 0; right: 0; top: 182px; text-align: center; font-size: 22px;
  }
  .address {
    position: absolute; left: 0; right: 0; top: 258px; text-align: center;
    color: var(--grey); font-size: 11.5px; letter-spacing: 0.8px;
  }
</style>
</head>
<body>

<section class="card card--front" aria-label="Card front">
  <svg class="front-art" viewBox="0 0 600 343" preserveAspectRatio="none">
    <path class="swoosh" d="M20 325 C 200 250, 360 120, 600 40 L 600 58 C 380 140, 230 265, 40 330 Z" fill="var(--swoosh)"/>
    <circle cx="125" cy="135" r="120" fill="var(--red)" opacity="0.85" role="img" aria-label="Large brand emblem area"/>
    <rect x="0" y="295" width="600" height="3" fill="var(--red)" transform="rotate(-3.2 600 295)"/>
  </svg>

  <div class="holder">
    <div class="holder__name">Mr. TOMAS VERLINDE</div>
    <div class="holder__title">VICE-PRESIDENT</div>
  </div>

  <div class="contact">
    <div><span class="contact__label">cell:</span> 908-555-0193</div>
    <div><span class="contact__label">office:</span> 1-855-555-0148 X 312</div>
    <div><span class="contact__label">email:</span> tomas@brivolentaxis.com</div>
  </div>

  <div class="brand brand--front">BRIVOLEN TAXIS</div>
</section>

<section class="card card--back" aria-label="Card back">
  <svg class="back-mark" viewBox="0 0 130 130" aria-hidden="true">
    <circle cx="65" cy="65" r="62" fill="var(--red)"/>
  </svg>
  <div class="brand brand--back">BRIVOLEN TAXIS</div>
  <p class="address">3187 Corwick Lane, Suite 412 Ashbury Falls, NJ 07999</p>
</section>

</body>
</html>
```